Lumo Brew Premium Matcha brand Label

This is a label design project for a luxury tea brand. Feel free to be creative within the guidelines.
Attached to this project is a document called “Private Label Design Requirements” with the design guidelines and template. There is another document called "Lumo Brew Packaging Instructions" this has more details necessary to stick to the guidelines in the first document.

I have also attached the certifications to be included as well as different variations of the logo for you to use.

If you have any questions, I am here.
Updates

Target Market(s)

Young, active, fun, enjoy the finer things

```html
<!DOCTYPE html>
<html lang="en">
<head>
<meta charset="utf-8">
<title>Lumo Brew Ceremonial Matcha Label</title>
<link rel="stylesheet" href="https://fonts.googleapis.com/css2?family=Raleway:wght@600;700&display=swap">
<style>
  :root {
    --page-bg: #bec9b8;
    --leaf-dark: #2f6a1c;
    --leaf-mid: #4f9a2a;
    --leaf-light: #8cc63f;
    --panel: #ffffff;
    --brand-green: #4a5e1f;
    --ink: #1c1c1c;
    --badge-green: #2e8b3e;
    --badge-blue: #3a7bd5;
  }
  * { box-sizing: border-box; margin: 0; padding: 0; }
  html, body { width: 1200px; height: 803px; overflow: hidden; }
  body {
    background: var(--page-bg);
    font-family: "Raleway", Arial, sans-serif;
    position: relative;
  }
  .label {
    position: absolute;
    left: 51px; top: 294px;
    width: 1098px; height: 214px;
    overflow: hidden;
    box-shadow: 0 6px 12px rgba(0, 0, 0, 0.18);
  }
  .leaf-photo {
    position: absolute; inset: 0;
    background:
      radial-gradient(ellipse at 20% 30%, var(--leaf-light) 0%, transparent 45%),
      radial-gradient(ellipse at 75% 70%, var(--leaf-light) 0%, transparent 40%),
      radial-gradient(ellipse at 50% 50%, var(--leaf-mid) 0%, transparent 70%),
      linear-gradient(135deg, var(--leaf-dark), var(--leaf-mid) 50%, var(--leaf-dark));
  }
  .panel { position: absolute; background: var(--panel); }
  .distributor {
    left: 73px; top: 71px; width: 226px; height: 73px;
    padding: 12px 11px;
    color: var(--brand-green);
    font-weight: 700; font-size: 9.4px; line-height: 15.8px;
    white-space: nowrap;
  }
  .front {
    left: 459px; top: 17px; width: 179px; height: 179px;
    padding: 18px;
  }
  .front-frame {
    width: 100%; height: 100%;
    border: 2px solid var(--brand-green);
    display: flex; flex-direction: column; align-items: center;
    text-align: center;
  }
  .brand-name {
    margin-top: 62px;
    font-size: 16px; font-weight: 700; color: var(--ink);
    line-height: 18px;
  }
  .product-name {
    margin-top: 4px;
    font-size: 11.5px; font-weight: 700; line-height: 14.5px;
    color: var(--brand-green);
    white-space: nowrap;
  }
  .net-weight {
    margin-top: auto; margin-bottom: 4px;
    font-size: 7.5px; font-weight: 700; color: var(--ink);
  }
  .cert { position: absolute; }
  .cert-round {
    left: 700px; top: 135px; width: 32px; height: 32px;
    border-radius: 50%; background: var(--panel);
    border: 3px solid var(--badge-green);
  }
  .cert-square {
    left: 737px; top: 136px; width: 36px; height: 27px;
    background: var(--badge-blue); border: 2px solid var(--panel);
  }
  .details {
    left: 781px; top: 42px; width: 248px; height: 130px;
    padding: 10px 10px;
    color: var(--ink);
    white-space: nowrap;
  }
  .details h2 {
    font-size: 11.5px; font-weight: 700; color: var(--brand-green);
    line-height: 15px;
  }
  .details p, .details li {
    font-size: 9.6px; font-weight: 700; line-height: 12px;
  }
  .details p { margin: 3px 0 7px 9px; }
  .details ul { list-style: none; margin-left: 9px; margin-top: 1px; }
  .details li::before { content: "\2022\00a0"; font-size: 7px; vertical-align: 1px; }
</style>
</head>
<body>
  <div class="label">
    <div class="leaf-photo" role="img" aria-label="Close-up photograph of fresh green tea leaves"></div>

    <div class="panel distributor">
      <div>Distributed by Lumo Brew Co. | Atlanta, Ga</div>
      <div>Certified Organic by Orin</div>
      <div>PRODUCT OF JAPAN</div>
    </div>

    <div class="panel front">
      <div class="front-frame">
        <div class="brand-name">Lumo Brew</div>
        <div class="product-name">PREMIUM ORGANIC<br>CEREMONIAL MATCHA</div>
        <div class="net-weight">Net Wt: 30g</div>
      </div>
    </div>

    <div class="cert cert-round" aria-label="Organic certification badge"></div>
    <div class="cert cert-square" aria-label="Non-GMO verification badge"></div>

    <div class="panel details">
      <h2>Ingredients</h2>
      <p>Premium Organic Japanese Matcha Green Tea</p>
      <h2>Instructions</h2>
      <ul>
        <li>2 tsp of Matcha</li>
        <li>2oz of Water (170-180 degrees F)</li>
        <li>Whisk in a W formation until frothy</li>
        <li>Sweeten to taste</li>
      </ul>
    </div>
  </div>
</body>
</html>
```